New Flyer Design for Residential Construction Loans

This specific flyer will be used for customers needing construction financing for Site Built Homes, I will attach a version of our Site Built flyer we have used with our former company (Bel Tarro Financial) Please use the same logo and contact information for Hollowmere Financial as shown on the Hollowmere Manufactured/Modular Flyer. On this Site-Built flyer, I'd like to see a couple of new ideas... As you see on the Hollowmere logo, there is a sail. Hollowmere is a sailing term. Looking for some graphics that would incorporate something like a sail. Have fun.
Target Market(s)
Customers seeking a construction loan
Look and feel

```html
<!DOCTYPE html>
<html lang="en">
<head>
<meta charset="utf-8">
<title>Hollowmere Financial – One-Time Close Construction Loans</title>
<link href="https://fonts.googleapis.com/css2?family=Poppins:wght@300;400;500;600;700;800&family=Oswald:wght@500;600&display=swap" rel="stylesheet">
<style>
  :root{
    --navy:#173a63;
    --navy-deep:#0f2a4a;
    --teal:#16a3b6;
    --teal-bright:#08c0d4;
    --ink:#2b2f36;
    --row-a:#e4e4e4;
    --row-b:#ececec;
    --grey-band:#ececec;
    --page:#e6e6e6;
    --white:#ffffff;
  }
  *{box-sizing:border-box;margin:0;padding:0}
  html,body{width:1200px;height:2400px;overflow:hidden}
  body{background:var(--page);font-family:"Poppins",sans-serif;color:var(--ink);position:relative}
  .flyer{position:absolute;left:50px;top:488px;width:1100px;height:1424px;background:var(--white);overflow:hidden;box-shadow:0 6px 24px rgba(0,0,0,.12)}
  .abs{position:absolute}
  .backdrop{left:0;top:0;width:1100px;height:620px}

  .brand{left:64px;top:92px}
  .brand-name{display:flex;align-items:center;gap:12px;font-weight:600;font-size:40px;line-height:1;color:var(--navy);letter-spacing:.5px}
  .brand-mark{width:32px;height:32px;background:var(--navy);display:inline-block}

  .photo{left:600px;top:150px;width:500px;height:420px}

  .headline{color:var(--white);white-space:nowrap}
  .headline.pre{left:66px;top:236px;font-weight:300;font-size:56px;line-height:1;letter-spacing:1px}
  .headline.main{left:66px;top:300px;font-weight:800;font-size:66px;line-height:1}
  .headline.big{left:62px;top:346px;font-weight:800;font-size:152px;line-height:1;color:var(--teal-bright);letter-spacing:1px}
  .headline.sub{left:68px;top:500px;font-weight:600;font-size:25px;line-height:1}

  .badge{left:772px;top:442px;width:268px;height:268px}
  .badge-text{left:772px;top:500px;width:268px;text-align:center;color:var(--white)}
  .badge-text .line{font-weight:700;font-size:25px;line-height:1.22}
  .badge-text .avail{font-family:"Oswald",sans-serif;font-weight:600;font-size:44px;line-height:1.1;color:var(--navy-deep)}

  .benefits-title{left:68px;top:602px;display:flex;align-items:center;gap:18px}
  .benefits-title h2{font-weight:800;font-size:32px;color:var(--navy);letter-spacing:.3px}
  .benefits-title h2 span{color:var(--teal)}
  .benefits-title .rule{width:325px;height:2px;background:var(--teal);position:relative}
  .benefits-title .rule::after{content:"";position:absolute;right:-4px;top:-3px;width:8px;height:8px;border-radius:50%;background:var(--teal)}

  .benefit-list{list-style:none;font-size:18px;line-height:1.2;color:var(--ink);white-space:nowrap}
  .benefit-list li{position:relative;padding-left:23px;margin-bottom:7px}
  .benefit-list li svg{position:absolute;left:0;top:5px;width:14px;height:14px}
  .col-left{left:68px;top:675px}
  .col-right{left:556px;top:675px}

  .rates{left:64px;top:887px;width:974px;border-collapse:collapse;border-radius:10px;overflow:hidden;table-layout:fixed}
  .rates th{background:var(--teal);color:var(--white);font-weight:700;font-size:21px;height:41px;letter-spacing:.3px}
  .rates td{height:62px;text-align:center;font-size:19px}
  .rates tr:nth-child(1) td{background:var(--row-a)}
  .rates tr:nth-child(2) td{background:var(--row-b)}
  .rates td.label{text-align:left;padding-left:25px;font-weight:500;font-size:21px}
  .rates td:nth-child(2),.rates td:nth-child(4){background:var(--row-b)}
  .rates tr:nth-child(2) td:nth-child(2),.rates tr:nth-child(2) td:nth-child(4){background:var(--row-a)}
  .rates .note{display:block;color:var(--teal);font-size:14px;line-height:1}
  .rates col.c1{width:326px}.rates col.c2{width:218px}.rates col.c3{width:214px}.rates col.c4{width:216px}

  .cta{left:112px;top:1067px;width:876px;height:40px;background:var(--navy);color:var(--white);text-align:center;font-weight:700;font-size:21px;letter-spacing:5px;line-height:40px;border-radius:0 0 30px 30px}

  .contact{top:1142px;display:flex;gap:26px;align-items:flex-start}
  .contact-left{left:74px}
  .contact-right{left:566px}
  .portrait{width:170px;height:150px;flex:none}
  .contact-info{padding-top:12px;font-size:15px;line-height:1.3;color:var(--ink)}
  .contact-info .name{font-family:"Oswald",sans-serif;font-weight:600;font-size:25px;color:var(--navy);line-height:1.1;letter-spacing:.2px}
  .contact-info .row{display:flex;align-items:center;gap:6px;white-space:nowrap}
  .contact-info .row.phones{gap:16px;margin-top:2px}
  .contact-info .strong{font-weight:700;font-size:18px}
  .contact-info svg{width:13px;height:13px;flex:none}
  .contact-info .email{font-weight:500}

  .legal{left:64px;top:1312px;width:980px;font-size:11px;line-height:1.32;color:#3a3a3a}
</style>
</head>
<body>
<main class="flyer">

  <svg class="abs backdrop" viewBox="0 0 1100 620" aria-hidden="true">
    <polygon points="500,203 700,0 1000,0 790,203" fill="var(--grey-band)"/>
    <polygon points="920,120 1030,0 1100,0 1100,30 980,150" fill="var(--grey-band)"/>
    <polygon points="1030,0 1100,0 1100,520 990,470" fill="var(--teal-bright)"/>
    <polygon points="0,203 810,203 640,571 0,571" fill="var(--navy)"/>
    <polygon points="0,203 810,203 780,270 0,330" fill="var(--navy-deep)" opacity=".35"/>
  </svg>

  <div class="abs brand">
    <div class="brand-name"><span class="brand-mark"></span>HOLLOWMERE FINANCIAL</div>
  </div>

  <svg class="abs photo" viewBox="0 0 500 420" role="img" aria-label="Photo of two construction workers in hard hats and safety vests reviewing building plans">
    <defs>
      <linearGradient id="photoTone" x1="0" y1="0" x2="1" y2="1">
        <stop offset="0" stop-color="#f2a23a"/>
        <stop offset=".55" stop-color="#e07a22"/>
        <stop offset="1" stop-color="#4a5566"/>
      </linearGradient>
    </defs>
    <polygon points="210,60 360,0 500,20 470,330 380,420 40,420 150,180" fill="url(#photoTone)"/>
  </svg>

  <div class="abs headline pre">ONE-TIME CLOSE</div>
  <div class="abs headline main">CONSTRUCTION</div>
  <div class="abs headline big">LOANS</div>
  <div class="abs headline sub">Unique Financing for Site-Built Homes</div>

  <svg class="abs badge" viewBox="0 0 200 200" aria-hidden="true">
    <polygon fill="var(--teal-bright)" points="100,4 116,20 137,12 145,33 167,33 167,55 188,63 180,84 196,100 180,116 188,137 167,145 167,167 145,167 137,188 116,180 100,196 84,180 63,188 55,167 33,167 33,145 12,137 20,116 4,100 20,84 12,63 33,55 33,33 55,33 63,12 84,20"/>
  </svg>
  <div class="abs badge-text">
    <div class="line">FHA, VA, and</div>
    <div class="line">Conventional</div>
    <div class="line">Financing</div>
    <div class="avail">AVAILABLE</div>
  </div>

  <div class="abs benefits-title">
    <h2>PROGRAM <span>BENEFITS</span></h2>
    <div class="rule"></div>
  </div>

  <ul class="abs benefit-list col-left">
    <li><svg viewBox="0 0 16 16"><circle cx="8" cy="8" r="8" fill="var(--teal)"/><path d="M4.5 8.3l2.3 2.2 4.7-4.8" stroke="#fff" stroke-width="2" fill="none"/></svg>Permanent Loan is closed one time, upfront,<br>before construction begins</li>
    <li><svg viewBox="0 0 16 16"><circle cx="8" cy="8" r="8" fill="var(--teal)"/><path d="M4.5 8.3l2.3 2.2 4.7-4.8" stroke="#fff" stroke-width="2" fill="none"/></svg>Save money with only one appraisal<br>and one closing</li>
    <li><svg viewBox="0 0 16 16"><circle cx="8" cy="8" r="8" fill="var(--teal)"/><path d="M4.5 8.3l2.3 2.2 4.7-4.8" stroke="#fff" stroke-width="2" fill="none"/></svg>Purchase of land can be rolled into the loan if it<br>is not already owned</li>
    <li><svg viewBox="0 0 16 16"><circle cx="8" cy="8" r="8" fill="var(--teal)"/><path d="M4.5 8.3l2.3 2.2 4.7-4.8" stroke="#fff" stroke-width="2" fill="none"/></svg>Gifts or land equity allowed for down payment</li>
  </ul>
  <ul class="abs benefit-list col-right">
    <li><svg viewBox="0 0 16 16"><circle cx="8" cy="8" r="8" fill="var(--teal)"/><path d="M4.5 8.3l2.3 2.2 4.7-4.8" stroke="#fff" stroke-width="2" fill="none"/></svg>15- and 30-year<br>permanent loan terms offered</li>
    <li><svg viewBox="0 0 16 16"><circle cx="8" cy="8" r="8" fill="var(--teal)"/><path d="M4.5 8.3l2.3 2.2 4.7-4.8" stroke="#fff" stroke-width="2" fill="none"/></svg>You will only work with construction loan<br>specialists</li>
    <li><svg viewBox="0 0 16 16"><circle cx="8" cy="8" r="8" fill="var(--teal)"/><path d="M4.5 8.3l2.3 2.2 4.7-4.8" stroke="#fff" stroke-width="2" fill="none"/></svg>Fast loan qualification and streamlined process</li>
    <li><svg viewBox="0 0 16 16"><circle cx="8" cy="8" r="8" fill="var(--teal)"/><path d="M4.5 8.3l2.3 2.2 4.7-4.8" stroke="#fff" stroke-width="2" fill="none"/></svg>Interest-only payments during construction<br>(must be paid by builder for VA Loans)</li>
  </ul>

  <table class="abs rates">
    <colgroup><col class="c1"><col class="c2"><col class="c3"><col class="c4"></colgroup>
    <thead><tr><th></th><th>FHA</th><th>CONVENTIONAL</th><th>VA</th></tr></thead>
    <tbody>
      <tr><td class="label">MINIMUM FICO SCORES</td><td>640<span class="note">620 with 90% Max LTV</span></td><td>640</td><td>640</td></tr>
      <tr><td class="label">DOWN PAYMENT AMOUNT</td><td>As low as 3.5% down</td><td>As low as 5%</td><td>100% Financing</td></tr>
    </tbody>
  </table>

  <div class="abs cta">CALL OR EMAIL TODAY FOR MORE INFORMATION</div>

  <section class="abs contact contact-left">
    <svg class="portrait" viewBox="0 0 170 150" role="img" aria-label="Headshot of loan officer Derek Amsel">
      <polygon points="42,0 128,0 170,75 128,150 42,150 0,75" fill="#d9e6ea"/>
      <polygon points="50,12 120,12 156,75 120,138 50,138 14,75" fill="#8fa3b3"/>
    </svg>
    <div class="contact-info">
      <div class="name">DEREK AMSEL</div>
      <div>Senior Loan Originator</div>
      <div>NMLS# 40217</div>
      <div class="row phones">
        <span class="row strong"><svg viewBox="0 0 16 16"><path d="M3 2h3l1.5 3.5-2 1.3a8 8 0 0 0 3.7 3.7l1.3-2L14 10v3a1 1 0 0 1-1 1A12 12 0 0 1 2 3a1 1 0 0 1 1-1z" fill="var(--teal)"/></svg>949-555-0142</span>
        <span class="row"><svg viewBox="0 0 16 16"><path d="M3 2h3l1.5 3.5-2 1.3a8 8 0 0 0 3.7 3.7l1.3-2L14 10v3a1 1 0 0 1-1 1A12 12 0 0 1 2 3a1 1 0 0 1 1-1z" fill="var(--teal)"/></svg>314-555-0187</span>
      </div>
      <div class="row"><svg viewBox="0 0 16 16"><rect x="4" y="1" width="8" height="4" fill="var(--teal)"/><rect x="1" y="6" width="14" height="6" rx="1" fill="var(--teal)"/><rect x="4" y="10" width="8" height="5" fill="var(--teal)"/></svg>888.555.0163</div>
      <div class="row email"><svg viewBox="0 0 16 16"><rect x="1" y="3" width="14" height="10" fill="var(--teal)"/><path d="M1 3l7 6 7-6" stroke="#fff" stroke-width="1.4" fill="none"/></svg>damsel@hollowmerefinancial.com</div>
    </div>
  </section>

  <section class="abs contact contact-right">
    <svg class="portrait" viewBox="0 0 170 150" role="img" aria-label="Headshot of builder sales manager Glen Harwick">
      <polygon points="42,0 128,0 170,75 128,150 42,150 0,75" fill="#d9e6ea"/>
      <polygon points="50,12 120,12 156,75 120,138 50,138 14,75" fill="#8fa3b3"/>
    </svg>
    <div class="contact-info">
      <div class="name">GLEN HARWICK</div>
      <div>Builder Sales Manager</div>
      <div>NMLS# 1405563</div>
      <div class="row phones">
        <span class="row strong"><svg viewBox="0 0 16 16"><path d="M3 2h3l1.5 3.5-2 1.3a8 8 0 0 0 3.7 3.7l1.3-2L14 10v3a1 1 0 0 1-1 1A12 12 0 0 1 2 3a1 1 0 0 1 1-1z" fill="var(--teal)"/></svg>760-555-0119</span>
        <span class="row">949-555-0176</span>
      </div>
      <div class="row"><svg viewBox="0 0 16 16"><rect x="4" y="1" width="8" height="4" fill="var(--teal)"/><rect x="1" y="6" width="14" height="6" rx="1" fill="var(--teal)"/><rect x="4" y="10" width="8" height="5" fill="var(--teal)"/></svg>888.555.0163</div>
      <div class="row email"><svg viewBox="0 0 16 16"><rect x="1" y="3" width="14" height="10" fill="var(--teal)"/><path d="M1 3l7 6 7-6" stroke="#fff" stroke-width="1.4" fill="none"/></svg>gharwick@hollowmerefinancial.com</div>
    </div>
  </section>

  <p class="abs legal">Glen Harwick NMLS #1405563 CA-DBO1405563 | Derek Amsel NMLS #40217 CA-DOC40217 Licensed by the Department of Business Oversight under the California Residential Mortgage Lending Act, 0901122, 100031450, LO3377, NM-Mortgage Loan Company License, TX-SML Mortgage Banker Registration, MLO-40217 Hollowmere Financial: NMLS 208814 | BK-0904418 | Information including the rates and fees contained in this advertisement are subject to change without notice. Offers subject to credit and property approval; program and other restrictions may apply. This is not an offer for extension of credit or a commitment to lend. Hollowmere Financial is not a government agency. www.hollowmerefinancial.com.</p>

</main>
</body>
</html>
```